WordPress Theme for "lxt graz" the large largest offically Recognized wine competition in the world

Our company "lxt graz" carries out the large largest offically Recognized wine competition in the world. We would like to redesign our existing website (www.lxt-fernhold.example). We use Drupal at the moment, but would like to move to WordPress. The site is in German and English (switchable). Following importent elements shoulderstand be in the design: - A timeline layout for awc year (example: https://www.lxt-fernhold.example/en/home at the bottom of the page). - Layout Elemenst for awards stars (example: https://www.lxt-fernhold.example/en/auszeichnungen at "Stars Winery"). - Layout for picture gallery - and all other elements of the origin site - ... footer content must be adjustable (example: https://www.lxt-fernhold.example/en/home at the bottom of the page). The wordpress theme must be adjustable (default colors, head pictures, partner logos, ...). The corporate design shoulderstand Be The Same Final result shoulderstand be a ready to use responsive WordPress theme. New ideas are welcome.

```html
<!DOCTYPE html>
<html lang="en">
<head>
<meta charset="utf-8">
<title>lxt graz – Wine Competition</title>
<link href="https://fonts.googleapis.com/css2?family=Open+Sans:wght@300;400;600;700&display=swap" rel="stylesheet">
<style>
:root{
  --black:#111111;
  --ink:#333333;
  --text:#666666;
  --muted:#999999;
  --line:#dddddd;
  --paper:#ffffff;
  --mist:#f1f1f1;
  --green:#a4b43c;
  --green-soft:#cfd99a;
  --chevron:#3a3a3a;
  --footer:#1c1c1c;
  --footer-base:#111111;
}
*{box-sizing:border-box;margin:0;padding:0}
html,body{width:1200px;height:3756px;overflow:hidden}
body{font-family:"Open Sans",Arial,sans-serif;color:var(--text);background:var(--paper);font-size:14px;line-height:1.6;position:relative}
.section{position:absolute;left:0;width:1200px}
.section-title{font-weight:300;text-transform:uppercase;color:var(--green);text-align:center;letter-spacing:1px;font-size:30px;line-height:1.2}

/* header */
.site-header{top:0;height:72px;background:var(--black);color:#fff}
.brand{position:absolute;left:60px;top:20px;display:flex;align-items:center;gap:12px}
.brand-mark{width:12px;height:12px;background:#fff}
.brand-name{font-size:26px;font-weight:600;letter-spacing:2px;line-height:1}
.meta-nav{position:absolute;right:60px;top:6px;display:flex;gap:22px;font-size:9px;color:#aaa;text-transform:uppercase}
.main-nav{position:absolute;right:60px;top:36px;display:flex;gap:30px;font-size:13px;font-weight:600;text-transform:uppercase}

/* hero */
.hero{top:72px;height:428px}
.hero-photo{position:absolute;inset:0;background:linear-gradient(180deg,#6a5630 0%,#b79a5e 35%,#d8c396 55%,#8a7245 80%,#4b3b22 100%)}
.hero-title{position:absolute;left:250px;top:216px;width:700px;padding:20px 0;background:rgba(30,30,30,.55);color:#fff;text-align:center;text-transform:uppercase;font-size:34px;font-weight:300;line-height:1.3}
.hero-title strong{font-weight:600}

/* app */
.app{top:500px;height:560px}
.app-title{position:absolute;left:100px;top:120px;width:600px;font-size:30px;font-weight:300;color:var(--green);text-transform:uppercase;line-height:1.3}
.app-text{position:absolute;left:100px;top:250px;width:560px;font-size:13px}
.btn-more{position:absolute;left:520px;top:380px;border:1px solid var(--green);color:var(--green);font-size:12px;padding:5px 14px}
.store-badges{position:absolute;left:100px;top:450px;display:flex;gap:14px}
.store-badge{width:100px;height:34px;border-radius:4px;background:#222}
.store-badge.alt{background:#3b6fb0}
.store-badge.red{background:#c02a2a}
.app-phone{position:absolute;left:740px;top:90px;width:200px;height:420px;border-radius:28px;background:linear-gradient(160deg,#2b2b2b,#000)}
.app-phone-screen{position:absolute;left:14px;top:50px;width:172px;height:310px;background:linear-gradient(180deg,#f7f4ea,#d9c58a)}
.app-seal{position:absolute;left:850px;top:320px;width:200px;height:200px;border-radius:50%;background:var(--black);border:4px solid #fff;color:#fff;text-align:center;padding-top:56px}
.app-seal b{display:block;font-size:17px;line-height:1.2}
.app-seal span{display:block;font-size:11px;color:#ccc;margin-top:6px;padding:0 30px}

/* timetable */
.timetable{top:1060px;height:540px;background:var(--mist)}
.timetable .section-title{position:absolute;top:112px;width:100%}
.tl-band{position:absolute;left:60px;top:340px}
.tl-entry{position:absolute;font-size:12px;color:var(--text);line-height:1.5}
.tl-entry b{display:block;color:var(--ink);font-weight:600;font-size:13px}
.tl-dots{position:absolute;width:0;border-left:1px dashed #aaa}

/* stars */
.stars{top:1600px;height:530px}
.stars-head{position:absolute;left:100px;top:150px;display:flex;align-items:center;gap:18px}
.stars-head h2{font-size:32px;font-weight:300;color:var(--green);text-transform:uppercase}
.stars-intro{position:absolute;left:100px;top:215px;width:480px;font-size:12px}
.stars-table{position:absolute;left:110px;top:270px;width:500px;border:1px solid var(--line)}
.stars-row{display:flex;align-items:center;height:44px;border-bottom:1px solid var(--line);padding-left:20px}
.stars-row:last-child{border-bottom:0}
.stars-row .icons{width:120px}
.stars-row span{font-style:italic;color:var(--green);font-size:18px;font-weight:300}
.stars-note{position:absolute;left:100px;top:430px;width:480px;font-size:12px}
.certificate{position:absolute;left:880px;top:20px;width:180px;height:350px;background:linear-gradient(180deg,#ffffff,#f3efe2 40%,#c8a94b 75%,#ece5cd);border:8px solid #2a2a2a}

/* special awards */
.awards{top:2130px;height:710px}
.awards .section-title{position:absolute;top:60px;width:100%}
.awards-intro{position:absolute;left:180px;top:124px;width:840px;text-align:center;font-size:12px}
.award-card{position:absolute;left:120px;width:960px;height:115px;border:1px solid var(--line);border-left:3px solid var(--green);padding:16px 24px;font-size:12px;box-shadow:0 2px 4px rgba(0,0,0,.06)}
.award-card h3{font-size:12px;font-weight:600;color:var(--green);text-transform:uppercase;margin-bottom:6px}

/* gallery */
.gallery{top:2840px;height:360px}
.gallery .section-title{position:absolute;top:20px;width:100%}
.gallery-row{position:absolute;left:60px;top:80px;display:flex;gap:8px}
.gallery-photo{width:264px;height:200px}
.gallery-dots{position:absolute;left:0;top:306px;width:100%;display:flex;justify-content:center;gap:8px}
.gallery-dots i{width:9px;height:9px;border-radius:50%;background:#aaa}
.gallery-dots i.on{background:#333}

/* partners */
.partners{top:3200px;height:240px;background:var(--mist)}
.partners .section-title{position:absolute;top:40px;width:100%}
.partner-list{position:absolute;left:100px;top:130px;width:1000px;display:flex;justify-content:space-between;align-items:center}
.partner-name{font-size:24px;font-weight:600;color:#8a8a8a}

/* footer */
.site-footer{top:3440px;height:260px;background:var(--footer);color:#bbb;font-size:11px;line-height:1.6}
.footer-col{position:absolute;top:36px}
.footer-col h4{font-size:14px;font-weight:600;color:#fff;text-transform:uppercase;margin-bottom:16px}
.footer-col p{margin-bottom:12px}
.newsletter-input{width:240px;height:30px;background:#fff;color:#999;padding:5px 10px;font-size:12px;margin-bottom:12px}
.newsletter-btn{display:inline-block;background:var(--green);color:#fff;font-size:12px;padding:5px 14px}
.footer-base{top:3700px;height:56px;background:var(--footer-base);color:#777;font-size:10px;text-align:center;line-height:56px}
</style>
</head>
<body>

<header class="section site-header">
  <div class="brand">
    <span class="brand-mark"></span>
    <span class="brand-name">LXT GRAZ</span>
  </div>
  <nav class="meta-nav"><span>English ▾</span><span>Contacts / Imprint</span><span>lxt graz Cellarbook App</span><span>Newsletter Subscription</span></nav>
  <nav class="main-nav"><span>News</span><span>The lxt graz</span><span>Awards</span><span>Participate</span><span>Downloads</span><span>Userlogin</span></nav>
</header>

<section class="section hero">
  <div class="hero-photo" role="img" aria-label="Photograph of a grand historic hall with gilded columns and chandeliers"></div>
  <h1 class="hero-title">The Largest<br><strong>Officially Recognized</strong><br>Wine Competition in the World</h1>
</section>

<section class="section app">
  <h2 class="app-title">lxt graz Cellarbook App<br>2016 Update!</h2>
  <p class="app-text">With the new LXT Cellarbook App you can see every award-winning wine from the last seasons at a glance. Search by producer, country, grape or medal, save your favourites and share them with friends. More than 12,000 wines are listed with tasting scores, producer details and direct links to every result.</p>
  <span class="btn-more">Read More »</span>
  <div class="store-badges">
    <span class="store-badge"></span><span class="store-badge alt"></span><span class="store-badge red"></span>
  </div>
  <div class="app-phone"><div class="app-phone-screen" role="img" aria-label="App screen showing the cellarbook cover with a wine glass"></div></div>
  <div class="app-seal"><b>LXT GRAZ<br>CELLARBOOK APP</b><span>Download for free for your Smartphone or Computer</span></div>
</section>

<section class="section timetable">
  <h2 class="section-title">Timetable 2017</h2>
  <div class="tl-entry" style="left:90px;top:200px"><b>registration for lxt graz</b>11 April - 1 May 2017</div>
  <div class="tl-entry" style="left:470px;top:200px"><b>lxt graz logistics center</b>Inspection &amp; Sorting<br>of 40,000 wine bottles</div>
  <div class="tl-entry" style="left:850px;top:180px"><b>Shipping of certificates</b>end of October</div>
  <div class="tl-entry" style="left:850px;top:246px"><b>lxt wine gala night 2017</b>at the City Hall of Graz<br>end of october</div>
  <div class="tl-dots" style="left:80px;top:204px;height:136px"></div>
  <div class="tl-dots" style="left:460px;top:204px;height:136px"></div>
  <div class="tl-dots" style="left:840px;top:184px;height:156px"></div>
  <svg class="tl-band" width="1080" height="40" viewBox="0 0 1080 40">
    <g fill="#3a3a3a">
      <polygon points="0,0 140,0 154,20 140,40 0,40"/>
      <polygon points="154,0 294,0 308,20 294,40 154,40 168,20"/>
      <polygon points="308,0 448,0 462,20 448,40 308,40 322,20"/>
      <polygon points="462,0 602,0 616,20 602,40 462,40 476,20"/>
      <polygon points="616,0 756,0 770,20 756,40 616,40 630,20"/>
      <polygon points="770,0 910,0 924,20 910,40 770,40 784,20"/>
      <polygon points="924,0 1066,0 1080,20 1066,40 924,40 938,20"/>
    </g>
    <g fill="#fff" font-family="Open Sans, Arial, sans-serif" font-size="14" text-anchor="middle">
      <text x="75" y="25">April</text><text x="235" y="25">May</text><text x="389" y="25">June</text>
      <text x="543" y="25">July</text><text x="697" y="25">August</text><text x="851" y="25">September</text><text x="1005" y="25">October</text>
    </g>
  </svg>
  <div class="tl-dots" style="left:270px;top:380px;height:26px"></div>
  <div class="tl-dots" style="left:660px;top:380px;height:26px"></div>
  <div class="tl-dots" style="left:840px;top:380px;height:26px"></div>
  <div class="tl-entry" style="left:180px;top:404px"><b>delivery of the wine samples</b>2 May – 24 May 2017</div>
  <div class="tl-entry" style="left:580px;top:404px"><b>tasting</b>by the jury<br>August 2017</div>
  <div class="tl-entry" style="left:850px;top:404px"><b>master tasting 2017</b>Beginning of September 2017</div>
</section>

<section class="section stars">
  <div class="stars-head">
    <h2>Stars Winery</h2>
    <svg width="170" height="46" viewBox="0 0 170 46" fill="#cfd99a">
      <polygon points="23,2 29,17 45,17 32,27 37,43 23,33 9,43 14,27 1,17 17,17"/>
      <polygon points="83,2 89,17 105,17 92,27 97,43 83,33 69,43 74,27 61,17 77,17"/>
      <polygon points="143,2 149,17 165,17 152,27 157,43 143,33 129,43 134,27 121,17 137,17"/>
    </svg>
  </div>
  <p class="stars-intro">From the 2017 competition onwards, the stars of a winery are calculated from its three best rated wines of the season.</p>
  <div class="stars-table">
    <div class="stars-row"><svg class="icons" width="100" height="22" viewBox="0 0 100 22" fill="#cfd99a"><polygon points="11,1 14,8 21,8 15,13 17,21 11,16 5,21 7,13 1,8 8,8"/><polygon points="41,1 44,8 51,8 45,13 47,21 41,16 35,21 37,13 31,8 38,8"/><polygon points="71,1 74,8 81,8 75,13 77,21 71,16 65,21 67,13 61,8 68,8"/></svg><span>Stars Winery: more than 346 total points</span></div>
    <div class="stars-row"><svg class="icons" width="100" height="22" viewBox="0 0 100 22" fill="#cfd99a"><polygon points="11,1 14,8 21,8 15,13 17,21 11,16 5,21 7,13 1,8 8,8"/><polygon points="41,1 44,8 51,8 45,13 47,21 41,16 35,21 37,13 31,8 38,8"/></svg><span>Stars Winery: more than 337 total points</span></div>
    <div class="stars-row"><svg class="icons" width="100" height="22" viewBox="0 0 100 22" fill="#cfd99a"><polygon points="11,1 14,8 21,8 15,13 17,21 11,16 5,21 7,13 1,8 8,8"/></svg><span>Stars Winery: more than 328 total points</span></div>
  </div>
  <p class="stars-note">The combined total of at least three wines is required; producers entering fewer wines are not listed in the star ranking.</p>
  <div class="certificate" role="img" aria-label="Gold award certificate with a wine glass illustration"></div>
</section>

<section class="section awards">
  <h2 class="section-title">lxt graz Special Awards 2016</h2>
  <p class="awards-intro">Only producers who submit at least six wines are considered for these special awards. Results are calculated automatically from the scores of the jury tasting.</p>
  <div class="award-card" style="top:190px"><h3>Best National Producer of the Year 2016</h3>The special award of lxt graz 2016 for the best wine producer of a country.<br>The points of the 6 maximum rated wines of a producer will be added.</div>
  <div class="award-card" style="top:325px"><h3>Best Organic Wine Producer of the Year 2016</h3>The special award of lxt graz 2016 for the best organic wine producer.<br>The points of the 6 maximum rated wines of an organic wine producer will be added.</div>
  <div class="award-card" style="top:460px"><h3>Bestretailer of the Year 2016</h3>The special award of lxt graz 2016 for the best retailer/importer.<br>The points of the 6 maximum rated wines of 3 different wine producers which were submitted by this retailer will be added.</div>
</section>

<section class="section gallery">
  <h2 class="section-title">Our Gallery</h2>
  <div class="gallery-row">
    <div class="gallery-photo" role="img" aria-label="Photograph of wine glasses lined up on a tasting table" style="background:linear-gradient(135deg,#c9bfae,#7b6a55)"></div>
    <div class="gallery-photo" role="img" aria-label="Photograph of rows of wine bottles in the logistics center" style="background:linear-gradient(135deg,#a39b8e,#4e463c)"></div>
    <div class="gallery-photo" role="img" aria-label="Photograph of jury members tasting wine" style="background:linear-gradient(135deg,#d7d2c8,#8c7f6d)"></div>
    <div class="gallery-photo" role="img" aria-label="Photograph of the tasting hall during the competition" style="background:linear-gradient(135deg,#bfb7a8,#6b6051)"></div>
  </div>
  <div class="gallery-dots"><i class="on"></i><i></i><i></i><i></i></div>
</section>

<section class="section partners">
  <h2 class="section-title">Our Partner</h2>
  <div class="partner-list">
    <span class="partner-name">Kelterhof</span>
    <span class="partner-name">Traubenwerk</span>
    <span class="partner-name">Corvella</span>
    <span class="partner-name">Rebstock</span>
    <span class="partner-name">Hallmayr</span>
  </div>
</section>

<footer class="section site-footer">
  <div class="footer-col" style="left:100px;width:300px">
    <h4>Impressum / Kontakt</h4>
    <p>Brandauer Kommunikation &amp; Event GmbH</p>
    <p>Kellerbergstraße 7<br>8010 Graz<br>Austria, Europe</p>
    <p>tel: +43 1 000 00 00<br>fax: +43 1 000 00 01<br>mobile: +43 660 000 00 00<br>e-mail: office@lxt-fernhold.example</p>
  </div>
  <div class="footer-col" style="left:420px;width:380px;padding-top:34px">
    <p>Partnerbüro Graz<br>Handelsagentur Nord, Musterweg 4<br>Geschäftszeiten Mo–Fr 9–17 Uhr<br>UID-Nr. ATU 00000000</p>
    <p>Webdesign / Technische Umsetzung<br>Studio Lindtal – Web &amp; Design<br>Layout Brandauer Kommunikation</p>
    <p>Hinweis: Alle Angaben ohne Gewähr.</p>
  </div>
  <div class="footer-col" style="left:840px;width:260px">
    <h4>Newsletter Abonnieren</h4>
    <div class="newsletter-input">Email</div>
    <span class="newsletter-btn">Abonnieren</span>
  </div>
</footer>
<div class="section footer-base">© 2017 lxt graz. All Rights Reserved. Terms of Use</div>

</body>
</html>
```